Operator Qualification Testing Flyer

I have a 8x10 basic flyer that I created usin InDesign for one of our services our company provides. I would like to see more options for the layout and general design of the flyer. This flyer will be used as a template for the other services we provide. I will include the InDesign Folder with all the logos and images. Please feel free to use any logo design within the folder and you can change the font and/or colors as needed. I would like the final output in a Indesign package folder to be used in InDesign 2021

Target Market(s)

Business to Business marketing in the Oil and Gas industry

Font styles to use
Sans Serif

Colors
85cae6
85acd3
3377b5
0355a3
0792cd
ffffff
cedeed

Requirements
Must have
• I included/attached a couple of brochures styles that I do like.

```html
<!DOCTYPE html>
<html lang="en">
<head>
<meta charset="utf-8">
<title>Pipeline OQ Testing Flyer</title>
<link href="https://fonts.googleapis.com/css2?family=Bebas+Neue&family=Montserrat:wght@700&family=Open+Sans:wght@400&family=Fira+Sans:wght@400;500&display=swap" rel="stylesheet">
<style>
  :root {
    --sky: #85cae6;
    --steel: #85acd3;
    --mid-blue: #3377b5;
    --brand-blue: #0355a3;
    --cyan: #0792cd;
    --white: #ffffff;
    --mist: #cedeed;
    --navy: #0b2f63;
    --ink: #2a3340;
    --stage: #dcdfe5;
    --photo-gray: #8a8a8a;
    --sign-yellow: #f5b400;
  }
  * { box-sizing: border-box; margin: 0; padding: 0; }
  html, body {
    width: 1200px; height: 2400px; overflow: hidden;
    background: var(--stage);
  }
  .flyer {
    position: absolute; left: 40px; top: 500px;
    width: 1120px; height: 1400px;
    background: var(--white);
    box-shadow: 0 18px 40px rgba(20, 30, 50, 0.25);
    overflow: hidden;
  }
  .brand {
    position: absolute; left: 36px; top: 0; height: 157px;
    display: flex; align-items: center; gap: 14px;
  }
  .brand-mark { width: 22px; height: 22px; background: var(--cyan); }
  .brand-name {
    font-family: "Fira Sans", sans-serif; font-weight: 500;
    font-size: 34px; color: var(--navy); letter-spacing: 0.5px;
  }
  .hero {
    position: absolute; left: 0; top: 157px; width: 1120px; height: 419px;
  }
  .hero-photo {
    position: absolute; inset: 0;
    background: linear-gradient(135deg, #9a9a9a 0%, #7c7c7c 55%, #6a6a6a 100%);
  }
  .hero-panel { position: absolute; inset: 0; }
  .hero-title {
    position: absolute; left: 705px; top: 112px;
    font-family: "Bebas Neue", sans-serif; font-size: 100px;
    line-height: 92px; color: var(--white); letter-spacing: 1px;
  }
  .hero-title .accent { color: var(--sky); }
  .content {
    position: absolute; left: 0; top: 576px; width: 1120px; height: 749px;
    background: linear-gradient(160deg, #e4eef8 0%, var(--mist) 45%, #bfd6ec 100%);
  }
  .copy {
    position: absolute; left: 35px; top: 48px; width: 702px;
  }
  .section-title {
    display: flex; align-items: center; gap: 18px;
    font-family: "Montserrat", sans-serif; font-weight: 700;
    font-size: 27px; color: var(--brand-blue);
    margin-bottom: 10px;
  }
  .section-title::before {
    content: ""; width: 21px; height: 19px; background: var(--brand-blue);
  }
  .section-text {
    font-family: "Open Sans", sans-serif; font-size: 19px;
    line-height: 27.5px; color: var(--ink); text-align: justify;
    margin-bottom: 20px;
  }
  .section-text + .section-text { margin-top: -2px; }
  .sign {
    position: absolute; left: 795px; top: 232px; width: 280px; height: 280px;
    border-radius: 50%;
    background: radial-gradient(circle at 50% 50%, var(--sign-yellow) 0%, #e9a800 70%, #1a1a1a 72%, #1a1a1a 100%);
  }
  .footer {
    position: absolute; left: 0; bottom: 0; width: 1120px; height: 75px;
    background: var(--brand-blue);
    display: flex; align-items: center; justify-content: space-between;
    padding: 0 38px;
    font-family: "Fira Sans", sans-serif; font-size: 22px; color: var(--white);
  }
  .contact { display: flex; align-items: center; gap: 9px; }
  .contact.phone { font-weight: 500; }
  .contact svg { fill: var(--white); }
</style>
</head>
<body>
  <main class="flyer">
    <header class="brand">
      <span class="brand-mark"></span>
      <span class="brand-name">Fieldline Assurance Inc.</span>
    </header>

    <section class="hero">
      <div class="hero-photo" role="img" aria-label="Aerial black and white photo of a pipeline trench with a yellow sideboom tractor and traffic cones"></div>
      <svg class="hero-panel" width="1120" height="419" viewBox="0 0 1120 419" aria-hidden="true">
        <defs>
          <linearGradient id="panelShade" x1="0" y1="0" x2="1" y2="1">
            <stop offset="0" stop-color="#0e3a78"/>
            <stop offset="1" stop-color="#0a2a5a"/>
          </linearGradient>
        </defs>
        <polygon points="600,0 1120,0 1120,419 716,419" fill="url(#panelShade)"/>
      </svg>
      <h1 class="hero-title">Pipeline<br><span class="accent">OQ</span> Testing</h1>
    </section>

    <section class="content">
      <div class="copy">
        <h2 class="section-title">What Is Operator Qualification?</h2>
        <p class="section-text">Operator Qualifications (OQ) for DOT Oil/Gas Pipelines are requirements set by Department of Transportation (DOT) and Pipeline and Hazardous Materials Safety Administration (PHMSA). To assure safety in the transport of hazardous gases and liquids in the nation’s pipelines, pipeline operators who perform covered tasks must be qualified. Qualified means that an individual has been evaluated and can perform assigned covered tasks and recognize and react to abnormal operating conditions.</p>

        <h2 class="section-title">What Are Covered Tasks?</h2>
        <p class="section-text">Covered tasks are defined in an operator’s written plan which defines specific job functions or activities personnel are qualified to perform on a pipeline facility.</p>

        <h2 class="section-title">What We Provide?</h2>
        <p class="section-text">Fieldline Assurance Inc. utilizes NQSB pipeline program to administer OQ assessment testing on 127 covered tasks. Upon completion of OQ testing the information is first transferred to NQSB’s Registry System and automatically uploaded to SafeLink.</p>
        <p class="section-text">In addition to the benefits provided by SafeLink’s database, the NQSB Registry System houses all the completion information allowing candidates to share their training information and employers to verify successful covered task and level completions.</p>
      </div>
      <div class="sign" role="img" aria-label="Round yellow petroleum pipeline warning marker sign"></div>
    </section>

    <footer class="footer">
      <span class="contact phone">
        <svg width="20" height="20" viewBox="0 0 24 24" aria-hidden="true"><path d="M6.6 10.8a15.1 15.1 0 0 0 6.6 6.6l2.2-2.2c.3-.3.7-.4 1-.2 1.1.4 2.3.6 3.6.6.6 0 1 .4 1 1V20c0 .6-.4 1-1 1C10.6 21 3 13.4 3 4c0-.6.4-1 1-1h3.5c.6 0 1 .4 1 1 0 1.3.2 2.5.6 3.6.1.3 0 .7-.2 1z"/></svg>
        406-555-0142
      </span>
      <span class="contact email">
        <svg width="24" height="18" viewBox="0 0 24 18" aria-hidden="true"><path d="M0 0h24v2L12 9 0 2z"/><path d="M0 4l12 7 12-7v14H0z"/></svg>
        owen@fieldline-assure.co
      </span>
    </footer>
  </main>
</body>
</html>
```